Roofing Company Business Card Design

My husband and I own our own roofing company. We specialise in the supply and installation of metal roofing, fascia, gutter, and downpipes.
I would like our design to somehow incorporate the above things. Having said that the logo also needs to be versatile. I need to be able to use it for uniforms, signage for building sites, and also signage for our cars. So I need it to look good on both a small and large scale.
Looking at logo styles I would like to use either pictorial/combination logo, or emblem logo. With this I would like to try and incorporate the initials "TSC" into this logo somehow.
I would like to use blue, black, and white as my colours.
Industry/Entity Type
Building
Logo Text
Tolvane Steel Cladding Pty Ltd
Logo styles of interest
Emblem Logo
Pictorial/Combination Logo

```html
<!DOCTYPE html>
<html lang="en">
<head>
<meta charset="utf-8">
<title>Tolvane Steel Cladding – Business Card</title>
<link rel="stylesheet" href="https://fonts.googleapis.com/css2?family=Arimo:wght@400;700&display=swap">
<style>
  :root {
    --bg: #eef0f2;
    --card: #ffffff;
    --navy: #04365f;
    --blue: #2a7cc2;
    --green: #62b946;
    --ink: #111111;
  }
  * { margin: 0; padding: 0; box-sizing: border-box; }
  html, body {
    width: 1200px;
    height: 693px;
    overflow: hidden;
    background: var(--bg);
    font-family: "Arimo", Arial, sans-serif;
  }
  .card {
    position: absolute;
    left: 40px;
    top: 43px;
    width: 1120px;
    height: 607px;
    background: var(--card);
    overflow: hidden;
  }
  .brand {
    position: absolute;
    left: 50px;
    top: 40px;
    display: flex;
    align-items: center;
    gap: 14px;
    color: var(--blue);
    font-weight: 700;
    font-size: 64px;
    letter-spacing: 2px;
  }
  .brand-mark {
    width: 26px;
    height: 26px;
    background: var(--blue);
  }
  .services {
    position: absolute;
    left: 362px;
    top: 42px;
    display: flex;
    gap: 11px;
    list-style: none;
    color: var(--blue);
    font-weight: 700;
    font-size: 21.5px;
    letter-spacing: 0.6px;
  }
  .services li {
    display: flex;
    align-items: center;
    gap: 13px;
    margin-right: 6px;
  }
  .services li::before {
    content: "";
    width: 15px;
    height: 15px;
    border-radius: 50%;
    background: var(--green);
  }
  .person {
    position: absolute;
    left: 0;
    right: 0;
    top: 166px;
    text-align: center;
  }
  .person-name {
    color: var(--navy);
    font-weight: 700;
    font-size: 47px;
    letter-spacing: 2px;
    line-height: 1.15;
    margin-left: 10px;
  }
  .person-role {
    color: var(--green);
    font-weight: 700;
    font-size: 35px;
    letter-spacing: 1px;
    margin-top: 6px;
    margin-left: 10px;
  }
  .contact {
    position: absolute;
    display: flex;
    align-items: flex-start;
    color: var(--blue);
    font-weight: 700;
    font-size: 27px;
    letter-spacing: 1px;
  }
  .contact svg { flex: none; }
  .contact-address { left: 70px; top: 314px; gap: 28px; line-height: 58px; }
  .contact-address svg { margin-top: 19px; }
  .contact-list {
    position: absolute;
    left: 740px;
    top: 307px;
    list-style: none;
  }
  .contact-list li {
    display: flex;
    align-items: center;
    gap: 22px;
    height: 62px;
    color: var(--blue);
    font-weight: 700;
    font-size: 27px;
    letter-spacing: 1px;
  }
  .contact-list svg { width: 24px; height: 24px; flex: none; }
  .footer-bands {
    position: absolute;
    left: 0;
    bottom: 0;
    width: 1120px;
    height: 115px;
  }
</style>
</head>
<body>
  <main class="card">
    <div class="brand">
      <span class="brand-mark"></span>
      <span class="brand-name">TSC</span>
    </div>

    <ul class="services">
      <li>METAL ROOFING</li>
      <li>FASCIA</li>
      <li>GUTTER</li>
      <li>DOWNPIPES</li>
    </ul>

    <section class="person">
      <h1 class="person-name">JOHN DOE</h1>
      <p class="person-role">Director</p>
    </section>

    <address class="contact contact-address" style="font-style:normal">
      <svg width="18" height="24" viewBox="0 0 18 24" aria-hidden="true">
        <path d="M9 1C4.6 1 1.5 4.2 1.5 8.4 1.5 14 9 23 9 23s7.5-9 7.5-14.6C16.5 4.2 13.4 1 9 1z" fill="var(--ink)"/>
        <circle cx="9" cy="8.5" r="2.8" fill="#fff"/>
      </svg>
      <span>Address goes<br>here.</span>
    </address>

    <ul class="contact-list">
      <li>
        <svg viewBox="0 0 24 24" aria-hidden="true">
          <circle cx="12" cy="12" r="10.5" fill="none" stroke="var(--ink)" stroke-width="1.6"/>
          <path d="M6 7c2 0 3 1 3 3s2 2 2 4-1 3-1 5M14 4c0 2 2 2 3 3s0 3 2 4M15 15c1 1 3 0 3 2" fill="none" stroke="var(--ink)" stroke-width="1.8"/>
        </svg>
        <span>www.tsc-cladding.com</span>
      </li>
      <li>
        <svg viewBox="0 0 24 24" aria-hidden="true">
          <path d="M7 2l3 1 0 5-2 1c0 3 2 6 4 7l2-1 4 2-1 4c-7 0-13-8-12-16z" fill="var(--ink)"/>
        </svg>
        <span>+000 000</span>
      </li>
      <li>
        <svg viewBox="0 0 24 24" aria-hidden="true">
          <rect x="2" y="5" width="20" height="14" fill="none" stroke="var(--ink)" stroke-width="1.8"/>
          <path d="M2 5l10 8 10-8M2 19l7-7M22 19l-7-7" fill="none" stroke="var(--ink)" stroke-width="1.6"/>
        </svg>
        <span>info@tsc-cladding.com</span>
      </li>
    </ul>

    <svg class="footer-bands" viewBox="0 0 1120 115" aria-hidden="true">
      <path d="M0 52 H520 L578 3 H1120 V115 H0 Z" fill="var(--navy)"/>
      <path d="M0 0 H560 L521 39 H0 Z" fill="var(--green)"/>
    </svg>
  </main>
</body>
</html>
```